Tarvolix new official website

We need a new design for our website www.tarvolix.com We are web marketing publishers and our website must be attractive for clients. That's why we need to "refresh" it. The main colour of our logo is orange, and this is an indication for the colours of the website too. We need the design for the homepage and the design of inner pages. Here is the list of the various sections of the website:
- ABOUT US: Who we are/Certificates/Offices/Team
- SERVICES: SEM/Display/Email Marketing and coregistration/ad networking
- PROJECTS/NETWORK/BRANDS: We need one page per country with screenshots of the websites and very short descriptions.
- TARVOLIX & CHARITY
- WORK WITH US
- CONTACT US
- NEWS

```html
<!DOCTYPE html>
<html lang="en">
<head>
<meta charset="utf-8">
<title>Tarvolix – The Main Way to Your Business</title>
<link rel="stylesheet" href="https://fonts.googleapis.com/css2?family=Open+Sans:wght@400;600;700&family=Titillium+Web:wght@300;400;700&family=Russo+One&display=swap">
<style>
:root{
  --orange:#f07d00;
  --orange-light:#ff9a1a;
  --frame:#474747;
  --nav:#3d3d3d;
  --ink:#222;
  --text:#555;
  --muted:#999;
  --line:#d5d5d5;
  --white:#fff;
}
*{margin:0;padding:0;box-sizing:border-box}
html,body{width:880px;height:1200px;overflow:hidden;background:var(--frame);font-family:"Open Sans",sans-serif;color:var(--text)}
.canvas{position:relative;width:880px;height:1200px}
.page{position:absolute;left:59px;top:0;width:765px;height:1117px;background:var(--white)}
.abs{position:absolute}
.header{position:absolute;left:59px;top:0;width:765px;height:92px;background:linear-gradient(#fff,#f3f3f3)}
.top-link{left:760px;top:9px;font-size:9px;color:var(--ink)}
.top-link::before{content:"";display:inline-block;border-left:4px solid #333;border-top:3px solid transparent;border-bottom:3px solid transparent;margin-right:6px}
.brand{left:92px;top:36px;display:flex;align-items:center;gap:5px;font-family:"Titillium Web",sans-serif;font-weight:700;font-size:25px;color:var(--orange)}
.brand i{width:14px;height:14px;border-radius:50%;background:var(--orange);display:block}
.search{left:573px;top:38px;width:237px;height:28px;border-radius:14px;background:#fafafa;border:1px solid #e2e2e2;box-shadow:inset 0 2px 4px rgba(0,0,0,.08)}
.search-btn{left:740px;top:41px;width:66px;height:21px;border-radius:11px;background:#111;color:#fff;font-size:8px;font-weight:700;display:flex;align-items:center;justify-content:center}
.nav{left:63px;top:95px;width:754px;height:45px;border-radius:12px;background:linear-gradient(#555,#2e2e2e);display:flex;overflow:hidden}
.nav a{color:#fff;text-decoration:none;font-size:11px;font-weight:600;display:flex;align-items:center;justify-content:center;border-left:1px dotted #6a6a6a;letter-spacing:.3px}
.nav a.active{background:linear-gradient(var(--orange-light),#e06c00);border:none}
.nav .end{width:14px;background:linear-gradient(var(--orange-light),#e06c00)}
.banner{left:77px;top:150px;width:730px;height:282px;border:1px solid #e5e5e5;background:#fff}
.device{left:80px;top:156px;width:160px;height:272px;border-radius:24px;background:linear-gradient(135deg,#555,#111 60%,#888)}
.haze{left:380px;top:200px;width:426px;height:150px;background:radial-gradient(ellipse at 70% 40%,rgba(240,125,0,.25),rgba(255,120,170,.18) 45%,rgba(255,255,255,0) 70%)}
.headline{left:314px;top:164px;font-family:"Titillium Web",sans-serif;font-weight:300;font-size:35px;color:#555;letter-spacing:.5px}
.headline b{font-weight:700;color:#3e3e3e}
.business{left:344px;top:206px;font-family:"Russo One",sans-serif;font-size:40px;color:var(--orange);letter-spacing:4px}
.cards{left:346px;top:286px;width:417px;height:204px;background:#fff;border-radius:10px;box-shadow:0 2px 8px rgba(0,0,0,.12)}
.card{position:absolute;top:0;width:208px;padding:14px 6px 0 10px}
.card+.card{border-left:1px dotted #ccc;top:14px;height:170px;padding-top:0}
.card h3{font-family:"Titillium Web",sans-serif;font-weight:400;font-size:16px;color:var(--ink);line-height:18px;padding-left:50px;height:40px;display:flex;flex-direction:column;justify-content:center;border-bottom:1px dotted #ccc;margin-bottom:12px;position:relative}
.card h3 span{color:var(--orange)}
.card h3::before{content:"";position:absolute;left:2px;top:6px;width:32px;height:28px;border-radius:6px;background:linear-gradient(#7aa7e8,#f39b2e)}
.card p{font-size:9px;line-height:14.4px;text-align:justify;color:var(--ink);letter-spacing:.3px}
.btn{background:#2e2e2e;color:#fff;font-size:8.5px;width:73px;height:23px;display:flex;align-items:center;justify-content:center;gap:6px}
.btn::after{content:"";border-left:3px solid #fff;border-top:3px solid transparent;border-bottom:3px solid transparent}
.section-title{font-family:"Titillium Web",sans-serif;font-weight:300;font-size:21px;color:#777;white-space:nowrap}
.section-title b{font-weight:700;color:var(--orange)}
.title-rule{height:5px;background:linear-gradient(90deg,#eee,#fff)}
.icon{border-radius:50%;background:radial-gradient(#fff,#cfcfcf);box-shadow:0 2px 4px rgba(0,0,0,.2)}
.vrule{border-left:1px dotted #bbb}
.expertise{left:86px;width:216px}
.expertise h4{font-size:11px;font-weight:400;color:var(--orange);margin-bottom:3px;padding-left:19px;position:relative}
.expertise h4::before{content:"";position:absolute;left:0;top:3px;width:9px;height:9px;background:linear-gradient(#bbb,#bbb) 4px 0/5px 5px no-repeat,linear-gradient(#999,#999) 0 4px/5px 5px no-repeat,linear-gradient(#bbb,#bbb) 4px 4px/5px 5px no-repeat}
.expertise p{font-size:8.5px;line-height:14.4px;text-align:justify;padding-left:19px;letter-spacing:.3px;color:#555}
.more{display:block;text-align:right;font-size:8.5px;color:var(--orange);margin-top:2px}
.more span{border-bottom:1px solid var(--orange);padding-bottom:1px}
.more span::after{content:"";display:inline-block;margin-left:4px;border-left:3px solid var(--orange);border-top:3px solid transparent;border-bottom:3px solid transparent}
.shots{left:372px;top:575px;width:396px;height:105px;background:linear-gradient(90deg,#dfe8f2,#cde0a8 20%,#2a2a2a 50%,#f0c020 55%,#3a3a3a 70%,#eee 90%,#fff)}
.arrow{width:24px;height:16px;border-radius:8px;background:#111}
.photo{left:362px;top:780px;width:168px;height:101px;border:1px solid #ddd;padding:3px;background:#fff;box-shadow:0 1px 3px rgba(0,0,0,.1)}
.photo div{width:100%;height:100%;background:linear-gradient(#4f8ad0,#a9c9e8 55%,#3d6b8f 75%,#2e4e63)}
.news-caption{left:340px;top:905px;width:210px;font-size:8.5px;color:#333;line-height:14.4px}
.adtech{left:593px;width:205px}
.adtech li{list-style:none;font-size:8.5px;line-height:14.4px;color:#444;padding-left:9px;position:relative;margin-bottom:14px;letter-spacing:.2px}
.adtech li::before{content:"";position:absolute;left:0;top:4px;border-left:3px solid var(--orange);border-top:3px solid transparent;border-bottom:3px solid transparent}
.contact{left:103px;top:962px;width:220px;font-size:8.4px;line-height:12.8px;color:#222}
.contact p{margin-bottom:12.8px}
.partners{left:357px;top:1018px;width:424px;height:90px;border-radius:22px;background:linear-gradient(#fff,#f4f4f4);border:1px solid #eee}
.badge{position:absolute}
.footer-nav{left:0;top:1136px;width:880px;text-align:center;font-size:9px;color:#bbb;font-weight:600;word-spacing:2px}
.footer-nav span{margin:0 5px;color:#888}
.footer-line{left:0;width:880px;text-align:center;font-size:8.5px;color:#9a9a9a}
</style>
</head>
<body>
<div class="canvas">
  <div class="page"></div>
  <header class="header"></header>
  <a class="abs top-link">Home</a>
  <div class="abs brand"><span>Tarvolix</span><i></i></div>
  <div class="abs search"></div>
  <div class="abs search-btn">SEARCH</div>

  <nav class="abs nav">
    <a class="active" style="width:104px">Home</a>
    <a style="width:94px">About Us</a>
    <a style="width:92px">Services</a>
    <a style="width:174px">Projects/ Network/ Brands</a>
    <a style="width:84px">TarvolixDiv</a>
    <a style="width:108px">Work with Us</a>
    <a style="width:84px">Email</a>
    <span class="end"></span>
  </nav>

  <section class="abs banner"></section>
  <div class="abs device" role="img" aria-label="Mobile phone with floating app icons"></div>
  <div class="abs haze" role="img" aria-label="Soft orange and pink smoke swirl"></div>
  <h1 class="abs headline">The <b>MAIN WAY</b> to Your</h1>
  <div class="abs business">BUSINESS</div>

  <div class="abs cards">
    <div class="card" style="left:0">
      <h3><span style="color:var(--ink)">Scope &amp; <span>Mission</span></span></h3>
      <p><b>Our aim is creating adding value</b> on our customers sales through technology and web marketing by means of the most modern web advertising systems. We help our customers in developing new sales...</p>
    </div>
    <div class="card" style="left:208px">
      <h3 style="margin-top:-14px;height:54px"><span style="color:var(--ink)">Clients' strategies &amp;</span><span style="text-align:right">web know how</span></h3>
      <p><b>We cooperate with the MAIN</b> international brands in the fields of tourism, finance, fashion, durable goods, technologies &amp; communication. We help our customers in finding the way to succeed...</p>
    </div>
  </div>
  <div class="abs btn" style="left:461px;top:476px">Read more</div>
  <div class="abs btn" style="left:671px;top:476px">Read more</div>

  <div class="abs icon" style="left:73px;top:445px;width:46px;height:46px"></div>
  <h2 class="abs section-title" style="left:125px;top:452px">Field of <b>EXPERTISE</b></h2>
  <div class="abs title-rule" style="left:125px;top:481px;width:180px"></div>
  <div class="abs vrule" style="left:326px;top:452px;height:640px"></div>

  <div class="abs expertise" style="top:513px">
    <h4>Tourism</h4>
    <p>Tourism has been our first passion.Today it is our MAIN business and generates our MAIN income.</p>
    <a class="more"><span>Read more</span></a>
  </div>
  <div class="abs expertise" style="top:593px">
    <h4>Technologies &amp; Communication</h4>
    <p>Dsl, laptops, hardware, isn't that a hard job to keep updated about it?.</p>
    <a class="more"><span>Read more</span></a>
  </div>
  <div class="abs expertise" style="top:659px">
    <h4>Finance</h4>
    <p>Tarvolix has been working for a long time with the MAIN brands in the international world of finance.</p>
    <a class="more"><span>Read more</span></a>
  </div>
  <div class="abs expertise" style="top:738px">
    <h4>Fashion</h4>
    <p>The new frontier for our company is the world of fashion; We believe that today, television and the Internet are merging...</p>
    <a class="more"><span>Read more</span></a>
  </div>
  <div class="abs expertise" style="top:827px">
    <h4>Durable Goods</h4>
    <p>As publisher we help the MAIN brands in the field of automotive, appliances, business equipment, electronic equipment...</p>
    <a class="more"><span>Read more</span></a>
  </div>

  <div class="abs icon" style="left:345px;top:528px;width:30px;height:30px;border-radius:6px;background:linear-gradient(#f7d27a,#e9a53a)"></div>
  <h2 class="abs section-title" style="left:386px;top:526px">Our <b>SITES/ BRANDS</b></h2>
  <div class="abs title-rule" style="left:386px;top:556px;width:170px"></div>
  <div class="abs arrow" style="left:342px;top:610px"><svg width="24" height="16"><path d="M15 4 L8 8 L15 12Z" fill="#fff"/></svg></div>
  <div class="abs shots" role="img" aria-label="Carousel of partner website screenshots"></div>
  <div class="abs arrow" style="left:778px;top:610px"><svg width="24" height="16"><path d="M9 4 L16 8 L9 12Z" fill="#fff"/></svg></div>

  <div class="abs icon" style="left:343px;top:727px;width:30px;height:32px;border-radius:6px;background:linear-gradient(#f7b04a,#d9751c)"></div>
  <h2 class="abs section-title" style="left:385px;top:731px">Tarvolix <b>NEWS</b></h2>
  <div class="abs title-rule" style="left:385px;top:758px;width:165px"></div>
  <div class="abs photo"><div role="img" aria-label="City skyline with a tall tower beside a river"></div></div>
  <div class="abs news-caption"><b>January 2009:</b> Opening of new branches in USA...<div style="text-align:right">[read more]</div></div>

  <div class="abs vrule" style="left:570px;top:727px;height:235px"></div>
  <div class="abs icon" style="left:588px;top:727px;width:30px;height:32px;border-radius:6px;background:linear-gradient(#f4c25a,#c9c9c9)"></div>
  <h2 class="abs section-title" style="left:627px;top:731px">Adtech <b>NEWS</b></h2>
  <div class="abs title-rule" style="left:627px;top:758px;width:170px"></div>
  <ul class="abs adtech" style="top:778px">
    <li>Social Design Strategy: Working from the Outside In Insights on what social media marketers should keep top of mind when helping businesses meaningfully engage with their ...</li>
    <li>Mediavant Buys AdLoomer, Bolsters Cross-Media Buying Tools Company aims to centralize buying and management of media, online and off.</li>
    <li>League Star Gives Social Advice to Draftees A veteran running back talks social media marketing with AdPulse</li>
  </ul>

  <div class="abs icon" style="left:75px;top:915px;width:40px;height:42px;border-radius:8px;background:linear-gradient(#f0f0f0,#e05a00)"></div>
  <h2 class="abs section-title" style="left:125px;top:920px">Contact <b style="font-weight:400">Us @</b></h2>
  <div class="abs title-rule" style="left:125px;top:947px;width:150px"></div>
  <div class="abs contact">
    <p><b>HEAD OFFICE:</b> Tarvolix srl - Via Lorenzi 14<br>65100 Verano (PE) - ITALY<br>Tel.+39 0855 550142 Fax +39 (0)2 5550 1873</p>
    <p><b>BRANCH OFFICE:</b> C-42 Lotus Park, Techhub<br>680412 Varanur - INDIA</p>
    <p style="margin:0"><b>BRANCH OFFICE:</b> Horizon House, Meridian Road<br>tel 01155501234 Delhi North - INDIA<br>BRANCH OFFICE: Carrer del Sol 18, 2-2<br>08010 Marenova - España</p>
  </div>

  <div class="abs partners">
    <div class="badge" style="left:34px;top:14px;width:62px;height:62px;border-radius:4px;background:var(--orange)"></div>
    <div class="badge" style="left:135px;top:28px;width:48px;height:34px;background:#e8e8e8"></div>
    <div class="badge" style="left:188px;top:34px;width:46px;height:22px;background:#c4161c"></div>
    <div class="badge" style="left:239px;top:30px;width:32px;height:32px;border-radius:50%;background:#d0101a"></div>
    <div class="badge" style="left:323px;top:17px;width:72px;height:52px;border-radius:4px;background:linear-gradient(#fff 55%,var(--orange-light) 55%);border:1px solid #e5e5e5"></div>
  </div>

  <div class="abs footer-nav">Home <span>/</span> About Us <span>/</span> Services <span>/</span> Projects/ Network/ Brands <span>/</span> TarvolixDiv <span>/</span> Work with Us <span>/</span> Email</div>
  <div class="abs footer-line" style="top:1160px">Tarvolix, Via Lorenzi, 14 - I-65100 Verano (PE) Italy,&nbsp;&nbsp; Tel.++39 0855 550142,&nbsp;&nbsp; Fax ++39 (0)2 5550 1873 , VAT IT 00000000000</div>
  <div class="abs footer-line" style="top:1179px">© Designed and developed by Tarvolix. 2011</div>
</div>
</body>
</html>
```